Nutrition Supplements needs Logo and Package Design

We need logo and label design for the new nutrition and dietary supplement brand called "Fern Ledger".
It is a new brand for western world but is based on 150 year old formulations successfully sold in the East.

The first five formulations are slated to be launched in the US in November.
They will aid in conditions like:
1. Product One: Diabetes,
2. Product Two: Heart Health,
3. Product Three: Men's Health & Vitality,
4. Product Four: Women's Health and Menstrual conditions,
5. Product Five: Sport Nutrition Aid in keeping mind and body agile.

The competition will be Brightmeadow own brands and brands like Kelpstone Path.

All the five products will be packaged in HDPE bottle ( 1 bottle has 60 capsules )
Height / length : 94.5 mm
Width : 51 mm

Please feel free to ask any additional questions.

Reason: We are new to this website and modes of operation. We have added participation budget to the project from today. We are also launching a project on pixel harbor for website design tomorrow. This website will be for the same products for which this packaging design project is launched. We are excited to find good designers on this platform that we can work with in the long term

Target Market(s)

Females in the age group 30 - 75.
Aware of nutrition supplements and their benefits, the label will have to stand out when it's next to brands like Brightmeadow, Kelpstone path etc.. in the nutrition isle.
shop at stores like RVT, Brightmeadow, Internet, Merchant Olly's, Pantry Lane.

Industry/Entity Type

Nutrition

Requirements
Nice to have
• It would be nice to have logo design that vibrates combination of freshness, power of traditional remedies, age old secrets, and age defiance.

```html
<!DOCTYPE html>
<html lang="en">
<head>
<meta charset="utf-8">
<title>Leafward Sage – Supplement Labels</title>
<link rel="stylesheet" href="https://fonts.googleapis.com/css2?family=Oswald:wght@500;700&family=Alegreya:wght@700&display=swap">
<style>
  :root {
    --page: #ffffff;
    --trim: #7a7a7a;
    --green-top: #86c94c;
    --green-bottom: #6ab232;
    --header-top: #ffffff;
    --header-bottom: #eef5e2;
    --brand-brown: #6b3a1c;
    --leaf: #8cc63f;
    --title-light: #ffffff;
    --title-shade: #d4d4d4;
    --tag-bg: #f6f2e2;
    --tag-text: #5b3a1e;
  }
  * { margin: 0; padding: 0; box-sizing: border-box; }
  html, body { width: 1200px; height: 485px; overflow: hidden; background: var(--page); }
  .sheet { position: relative; width: 1200px; height: 485px; }

  .trim-mark { position: absolute; height: 1px; background: var(--trim); }

  .label {
    position: absolute; top: 25px; width: 236px; height: 438px; overflow: hidden;
    background: linear-gradient(var(--header-top), var(--header-bottom) 110px);
  }
  .label-body { position: absolute; inset: 0; }

  .brand { position: absolute; top: 12px; left: 0; width: 100%; text-align: center; }
  .brand-dot { display: block; width: 34px; height: 34px; margin: 0 auto 10px; border-radius: 50%; background: var(--leaf); }
  .brand-name {
    font-family: "Alegreya", serif; font-weight: 700; font-size: 27px;
    color: var(--brand-brown); line-height: 1;
  }

  .product-title {
    position: absolute; left: 0; width: 100%; text-align: center;
    font-family: "Oswald", sans-serif; font-weight: 700; text-transform: uppercase;
    line-height: 1;
    background: linear-gradient(var(--title-light) 40%, var(--title-shade));
    -webkit-background-clip: text; background-clip: text; color: transparent;
    filter: drop-shadow(0 2px 2px rgba(0,0,0,0.25));
  }
  .product-title span { display: block; }

  .art { position: absolute; border-radius: 16px; }

  .count-tag {
    position: absolute; bottom: 0; left: 50%; transform: translateX(-50%); z-index: 2;
    width: 122px; height: 27px; border-radius: 10px 10px 0 0;
    background: var(--tag-bg); color: var(--tag-text);
    font-family: "Oswald", sans-serif; font-weight: 500; font-size: 18px;
    text-align: center; line-height: 28px;
  }

  .label--diabetic { left: 22px; }
  .label--heart { left: 479px; }
  .label--mens { left: 938px; }

  .label--diabetic .product-title { top: 136px; }
  .label--diabetic .line-main { font-size: 54px; letter-spacing: 0.5px; }
  .label--diabetic .line-sub { font-size: 35px; letter-spacing: 0.5px; margin-top: 2px; }
  .label--diabetic .art {
    left: 18px; top: 262px; width: 210px; height: 128px;
    background: linear-gradient(135deg, #4f8f2a 0%, #8a6a32 30%, #d2462e 55%, #e99a2a 78%, #f1c94a 100%);
  }

  .label--heart .product-title { top: 126px; font-size: 53px; }
  .label--heart .art {
    left: 32px; top: 245px; width: 172px; height: 155px;
    background: linear-gradient(180deg, #b9b3a8 0%, #e43a33 28%, #c61f1d 100%);
  }

  .label--mens .product-title { top: 116px; }
  .label--mens .line-main { font-size: 43px; }
  .label--mens .line-sub { font-size: 35px; }
  .label--mens .art {
    left: 42px; top: 247px; width: 180px; height: 191px; border-radius: 16px 16px 0 0;
    background: linear-gradient(180deg, #d9b89c 0%, #f1ede8 40%, #e9e9e9 62%, #2f3b4d 100%);
  }
</style>
</head>
<body>
<div class="sheet">
  <div class="trim-mark" style="left:288px;top:25px;width:58px"></div>
  <div class="trim-mark" style="left:391px;top:25px;width:58px"></div>
  <div class="trim-mark" style="left:743px;top:25px;width:58px"></div>
  <div class="trim-mark" style="left:851px;top:25px;width:58px"></div>
  <div class="trim-mark" style="left:288px;top:462px;width:58px"></div>
  <div class="trim-mark" style="left:391px;top:462px;width:58px"></div>
  <div class="trim-mark" style="left:743px;top:462px;width:58px"></div>
  <div class="trim-mark" style="left:851px;top:462px;width:58px"></div>

  <section class="label label--diabetic">
    <svg class="label-body" width="236" height="438" viewBox="0 0 236 438">
      <defs><linearGradient id="g1" x1="0" y1="0" x2="0" y2="1"><stop offset="0" stop-color="#86c94c"/><stop offset="1" stop-color="#6ab232"/></linearGradient></defs>
      <path d="M0,111 Q118,88 236,111 L236,438 L0,438 Z" fill="url(#g1)"/>
    </svg>
    <div class="brand"><span class="brand-dot"></span><div class="brand-name">Leafward Sage</div></div>
    <h2 class="product-title"><span class="line-main">Diabetic</span><span class="line-sub">Multivitamin</span></h2>
    <div class="art" role="img" aria-label="Basket of fresh fruit and vegetables"></div>
    <div class="count-tag">60 CAPSULES</div>
  </section>

  <section class="label label--heart">
    <svg class="label-body" width="236" height="438" viewBox="0 0 236 438">
      <defs><linearGradient id="g2" x1="0" y1="0" x2="0" y2="1"><stop offset="0" stop-color="#86c94c"/><stop offset="1" stop-color="#6ab232"/></linearGradient></defs>
      <path d="M0,111 Q118,88 236,111 L236,438 L0,438 Z" fill="url(#g2)"/>
    </svg>
    <div class="brand"><span class="brand-dot"></span><div class="brand-name">Leafward Sage</div></div>
    <h2 class="product-title"><span>Heart</span><span>Health</span></h2>
    <div class="art" role="img" aria-label="Cartoon red heart lifting a barbell"></div>
    <div class="count-tag">60 CAPSULES</div>
  </section>

  <section class="label label--mens">
    <svg class="label-body" width="236" height="438" viewBox="0 0 236 438">
      <defs><linearGradient id="g3" x1="0" y1="0" x2="0" y2="1"><stop offset="0" stop-color="#86c94c"/><stop offset="1" stop-color="#6ab232"/></linearGradient></defs>
      <path d="M0,111 Q118,88 236,111 L236,438 L0,438 Z" fill="url(#g3)"/>
    </svg>
    <div class="brand"><span class="brand-dot"></span><div class="brand-name">Leafward Sage</div></div>
    <h2 class="product-title"><span class="line-main">Men's</span><span class="line-main">Health</span><span class="line-sub">&amp; Vitality</span></h2>
    <div class="art" role="img" aria-label="Smiling man in a white tank top running"></div>
    <div class="count-tag">60 CAPSULES</div>
  </section>
</div>
</body>
</html>
```